Stationery Design Project

Would like to have the design elements we created in for our website (www.brook-holdings.example), incorporated in a stationery design layout.
Updates
Colors used in the logo attachments do not need to be used. We are open to different color variations. Looking for a crisp, clean, modern update using the design elements in attachments and which can also be viewed on or website.
A note to designers:
Project Deadline Extended
Reason: Due to update in our project description and requirements, we have decided to extend the deadline of this project to provide ample opportunity to all designers participating .
Requirements
Must have
- Must have continuity with the theme and design features used in our website. Have attached .jpg images of some of the design elements.

```html
<!DOCTYPE html>
<html lang="en">
<head>
<meta charset="utf-8">
<title>Brook Holdings Letterhead</title>
<link href="https://fonts.googleapis.com/css2?family=Arimo:wght@400;700&display=swap" rel="stylesheet">
<style>
  :root {
    --backdrop: #d9d9d7;
    --paper: #ffffff;
    --ink: #222222;
    --muted: #666666;
    --brand-blue: #1f7fc1;
    --grass-dark: #7fae4a;
    --grass-light: #c9df8f;
    --watermark: #ededed;
  }
  * { margin: 0; padding: 0; box-sizing: border-box; }
  html, body { width: 1200px; height: 849px; overflow: hidden; }
  body {
    background: var(--backdrop);
    font-family: "Arimo", Arial, sans-serif;
    color: var(--ink);
    position: relative;
  }
  .letter {
    position: absolute;
    left: 303px; top: 40px;
    width: 595px; height: 770px;
    background: var(--paper);
    box-shadow: 0 2px 8px rgba(0,0,0,0.25);
  }
  .header-band { position: absolute; left: 0; top: 28px; width: 352px; height: 58px; }
  .brand-name {
    position: absolute; left: 356px; top: 42px;
    font-size: 29px; font-weight: 400; color: var(--brand-blue);
    letter-spacing: -0.3px; white-space: nowrap;
  }
  .letter-body {
    position: absolute; left: 38px; top: 161px; width: 518px;
    font-size: 11.2px; line-height: 14px;
  }
  .letter-body p { text-align: justify; }
  .date { margin-bottom: 27px; }
  .recipient { margin-bottom: 28px; }
  .paragraph { margin-bottom: 14px; }
  .closing { margin-top: 33px; margin-bottom: 45px; }
  .footer-mark { position: absolute; left: 30px; top: 615px; width: 230px; height: 120px; }
  .contact-block {
    position: absolute; right: 40px; top: 658px;
    text-align: right; font-size: 7.4px; line-height: 10px; color: var(--muted);
  }
  .contact-block .company { color: var(--brand-blue); font-weight: 700; }
  .contact-block .label { color: var(--brand-blue); }
  .contact-block .web { color: var(--brand-blue); font-weight: 700; }
  .contact-block .gap { height: 10px; }
</style>
</head>
<body>
  <main class="letter">
    <svg class="header-band" viewBox="0 0 352 58" role="img" aria-label="Soft green grass photograph band">
      <defs>
        <linearGradient id="grass" x1="0" y1="0" x2="1" y2="0">
          <stop offset="0" stop-color="var(--grass-dark)"/>
          <stop offset="0.6" stop-color="var(--grass-light)"/>
          <stop offset="1" stop-color="#e6efc4"/>
        </linearGradient>
      </defs>
      <path d="M0 0 H352 C330 8 318 30 308 58 H0 Z" fill="url(#grass)"/>
    </svg>
    <div class="brand-name">Brook Holdings</div>

    <section class="letter-body">
      <p class="date">September 10, 2012</p>
      <p class="recipient">Ms. Clara Whitfield<br>Accounts Payable<br>The Copper Pan Co.<br>212 Harbor Market Way<br>Eastgate, CA 90999</p>
      <p>Dear Ms. Whitfield,</p>
      <p class="paragraph">It has come to my attention that your company, The Copper Pan Co. has been late with paying their invoices for the past three months.</p>
      <p class="paragraph">In order to encourage our customers to pay for their invoices before the due date, we have implemented a discount model where we'll give you 2% off your invoice if you pay us within 10 days of receiving the invoice.</p>
      <p>I hope that everything is going well for you and your company. You are one of our biggest customers, and we appreciate your business. If you have any questions, feel free to contact me at (555) 010-4477.</p>
      <p class="closing">Sincerely,</p>
      <p>Dan Mercer<br>Accounts Receivable</p>
    </section>

    <svg class="footer-mark" viewBox="0 0 230 120" role="img" aria-label="Faint decorative brand flourish">
      <defs>
        <radialGradient id="faint" cx="0.4" cy="0.5" r="0.6">
          <stop offset="0" stop-color="var(--watermark)"/>
          <stop offset="1" stop-color="var(--paper)"/>
        </radialGradient>
      </defs>
      <rect width="230" height="120" fill="url(#faint)"/>
    </svg>

    <address class="contact-block" style="font-style:normal">
      <div class="company">Brook Holdings, Inc.</div>
      <div>418 Alder Creek Road Suite 12</div>
      <div>Millbrook, GA 30999</div>
      <div>(555) 014-2290&nbsp; <span class="label">Phone</span></div>
      <div>(555) 014-2291&nbsp; <span class="label">Fax</span></div>
      <div class="gap"></div>
      <div>hello@brook-holdings.example&nbsp; <span class="label">E-mail</span></div>
      <div class="web">www.brook-holdings.example</div>
    </address>
  </main>
</body>
</html>
```